Create a premium soap bar box bar design for an all-natural, men's skincare brand.

We are launching a men’s premium, natural soap bar and skincare business. To start, we will be launching cold-press, all-natural soap bars with a few additional products such as lotions. We plan to expand our line into additional skincare products such as face exfoliants, moisturizers and cleansers that target basic needs such as anti-aging, clarifying and hydrating.

Our target audience is men ages 25-50, with a secondary audience of male teens. Our target audience are mid to high income, professionals that live in more urban areas, but enjoy being active outdoors after work and on the weekends. Our target audience are hard workers, humble and want to enjoy all that life has to offer – whether that’s on top of a mountain or an ocean wave. They hike, bike, skateboard, surf or any other sport that gets them outside. They are husbands, brothers and fathers – there for their family and friends.

Our brand is sophisticated, adventurous and has a sense of humor. Many of our competitors either focus on the rugged outdoors or are more pretentious. We are in-between. We are free spirited and love the fresh air. Our products are trustworthy with no toxic chemicals or harsh ingredients. We are all-natural and provide high-quality, premium products that our audience expects and deserves.

Target Market(s)

Men, ages 25-54 who are high-earning professionals, yet enjoy getting outdoors and being active on the weekends - hiking, biking, surfing, skateboarding and more.

Industry/Entity Type

Men's skincare

Font styles to use
Sans Serif

Requirements
Must have
• See attachments
Nice to have
• We would prefer to a have a premium, slightly more modern looking design that will appeal to our target audience and slightly higher price point.
Should not have
• Please do not include an icon for the fragrance, i.e. cinnamon sticks. However, we do need some differentiation for the fragrance, i.e. color, etc. as it will be on the shelf with other fragrances.

```html
<!DOCTYPE html>
<html lang="en">
<head>
<meta charset="utf-8">
<title>Ridge Hale Soap Bar Labels</title>
<link rel="stylesheet" href="https://fonts.googleapis.com/css2?family=Graduate&family=Jost:wght@400;500&family=Oswald:wght@500&display=swap">
<style>
  :root {
    --navy: #0f2740;
    --navy-deep: #0a1a2c;
    --kraft: #c9a87a;
    --kraft-light: #d9bd93;
    --ink: #1c2f4f;
    --white: #eef0f2;
    --bourbon: #8b0a0a;
    --citrus: #1c8a12;
    --cinnamon: #e06d10;
    --backdrop: #e9e5de;
  }
  * { box-sizing: border-box; margin: 0; padding: 0; }
  html, body { width: 1200px; height: 864px; overflow: hidden; }
  body {
    background: var(--backdrop);
    font-family: "Jost", sans-serif;
    position: relative;
  }
  .label {
    position: absolute;
    width: 560px;
    height: 300px;
    display: flex;
    box-shadow: 0 10px 28px rgba(0,0,0,.18);
  }
  .label--bourbon { left: 30px; top: 100px; --accent: var(--bourbon); }
  .label--citrus { left: 610px; top: 100px; --accent: var(--citrus); }
  .label--cinnamon { left: 320px; top: 440px; --accent: var(--cinnamon); }

  .brand-panel {
    width: 240px;
    background: linear-gradient(160deg, var(--navy) 0%, var(--navy-deep) 100%);
    display: flex;
    flex-direction: column;
    align-items: center;
    justify-content: center;
    gap: 14px;
  }
  .brand-mark {
    width: 56px; height: 56px;
    border-radius: 50%;
    border: 3px solid var(--white);
  }
  .brand-name {
    color: var(--white);
    font-family: "Jost", sans-serif;
    font-weight: 500;
    font-size: 24px;
    letter-spacing: 2px;
  }

  .product-panel {
    flex: 1;
    position: relative;
    border-left: 6px solid var(--accent);
    background: radial-gradient(ellipse at 40% 35%, var(--kraft-light) 0%, var(--kraft) 75%);
    padding: 26px 22px 0 26px;
  }
  .scent-name {
    font-family: "Graduate", serif;
    color: var(--accent);
    font-size: 42px;
    line-height: 40px;
    letter-spacing: 1px;
  }
  .scent-profile {
    margin-top: 12px;
    color: var(--ink);
    font-size: 17px;
    font-weight: 500;
    letter-spacing: 1.5px;
  }
  .soap-type {
    color: var(--ink);
    font-size: 14px;
  }
  .net-weight {
    position: absolute;
    left: 26px; bottom: 14px;
    color: var(--ink);
    font-size: 12px;
  }
  .grit-badge {
    position: absolute;
    right: 18px; bottom: 22px;
    width: 96px; height: 96px;
  }
  .grit-badge text {
    font-family: "Oswald", sans-serif;
    font-size: 13px;
    fill: var(--accent);
  }
</style>
</head>
<body>

<article class="label label--bourbon">
  <div class="brand-panel">
    <span class="brand-mark"></span>
    <span class="brand-name">RIDGE HALE</span>
  </div>
  <div class="product-panel">
    <h2 class="scent-name">BOUR<br>BON<br>VANILLA</h2>
    <p class="scent-profile">SWEET &amp; SPICY</p>
    <p class="soap-type">Men’s Natural Soap</p>
    <p class="net-weight">5 Oz. Bar</p>
    <svg class="grit-badge" viewBox="0 0 96 96">
      <circle cx="48" cy="48" r="30" fill="none" stroke="var(--ink)" stroke-width="1.5"/>
      <circle cx="48" cy="48" r="40" fill="none" stroke="var(--ink)" stroke-width="1.5" stroke-dasharray="10 8"/>
      <rect x="8" y="38" width="80" height="20" fill="var(--kraft)"/>
      <line x1="22" y1="38" x2="74" y2="38" stroke="var(--ink)" stroke-width="1.5"/>
      <line x1="22" y1="58" x2="74" y2="58" stroke="var(--ink)" stroke-width="1.5"/>
      <text x="48" y="53" text-anchor="middle">MEDIUM GRIT</text>
    </svg>
  </div>
</article>

<article class="label label--citrus">
  <div class="brand-panel">
    <span class="brand-mark"></span>
    <span class="brand-name">RIDGE HALE</span>
  </div>
  <div class="product-panel">
    <h2 class="scent-name">CITRUS<br>AND<br>CEDAR</h2>
    <p class="scent-profile">SWEET &amp; SPICY</p>
    <p class="soap-type">Men’s Natural Soap</p>
    <p class="net-weight">5 Oz. Bar</p>
    <svg class="grit-badge" viewBox="0 0 96 96">
      <circle cx="48" cy="48" r="30" fill="none" stroke="var(--ink)" stroke-width="1.5"/>
      <circle cx="48" cy="48" r="40" fill="none" stroke="var(--ink)" stroke-width="1.5" stroke-dasharray="10 8"/>
      <rect x="8" y="38" width="80" height="20" fill="var(--kraft)"/>
      <line x1="22" y1="38" x2="74" y2="38" stroke="var(--ink)" stroke-width="1.5"/>
      <line x1="22" y1="58" x2="74" y2="58" stroke="var(--ink)" stroke-width="1.5"/>
      <text x="48" y="53" text-anchor="middle">MEDIUM GRIT</text>
    </svg>
  </div>
</article>

<article class="label label--cinnamon">
  <div class="brand-panel">
    <span class="brand-mark"></span>
    <span class="brand-name">RIDGE HALE</span>
  </div>
  <div class="product-panel">
    <h2 class="scent-name">CINNA<br>MON<br>BARK</h2>
    <p class="scent-profile">SWEET &amp; SPICY</p>
    <p class="soap-type">Men’s Natural Soap</p>
    <p class="net-weight">5 Oz. Bar</p>
    <svg class="grit-badge" viewBox="0 0 96 96">
      <circle cx="48" cy="48" r="30" fill="none" stroke="var(--ink)" stroke-width="1.5"/>
      <circle cx="48" cy="48" r="40" fill="none" stroke="var(--ink)" stroke-width="1.5" stroke-dasharray="10 8"/>
      <rect x="8" y="38" width="80" height="20" fill="var(--kraft)"/>
      <line x1="22" y1="38" x2="74" y2="38" stroke="var(--ink)" stroke-width="1.5"/>
      <line x1="22" y1="58" x2="74" y2="58" stroke="var(--ink)" stroke-width="1.5"/>
      <text x="48" y="53" text-anchor="middle">MEDIUM GRIT</text>
    </svg>
  </div>
</article>

</body>
</html>
```